bottle label/ product label for smoothies (ultra fresh)

Please create a bottle label for our smoothies for retail distribution.
It's important that the following key features are clearly stated:

Ultra-fresh

Handmade

No preservatives

Not heat-treated

No added sugar

The base of the product label should be transparent, so that the color and content of the smoothie can be seen clearly.

We are a young, dynamic company. Our values are honesty, ultra-freshness, and authenticity — and we are the only ones producing this type of product in our country. We are positioned in the premium segment.

Design style: Modern, clean, and natural — but not playful or childish.

Example product: Kelu Kelu (Mango, Pineapple, Lemon, Passion Fruit, Orange)

Wenn du möchtest, kann ich auch gleich einen konkreten Vorschlag für das Etikettendesign auf Englisch oder einen Entwurfstext für das Label selbst erstellen. Sag einfach Bescheid!

Target Market(s)

trade - convenience

Industry/Entity Type

trade

Font styles to use
Sans Serif

Requirements
Must have
• sales- features: Ultra-fresh Handmade No preservatives Not heat-treated No added sugar

```html
<!DOCTYPE html>
<html lang="en">
<head>
<meta charset="UTF-8">
<title>verdalis – Apple Ultra-Fresh Label</title>
<link rel="stylesheet" href="https://fonts.googleapis.com/css2?family=Montserrat:wght@400;500;700&display=swap">
<style>
  :root {
    --bg: #ffffff;
    --ink: #111111;
    --ink-soft: #2a2a2a;
  }
  * { margin: 0; padding: 0; box-sizing: border-box; }
  html, body {
    width: 1200px;
    height: 1199px;
    overflow: hidden;
    background: var(--bg);
  }
  .canvas {
    position: relative;
    width: 1200px;
    height: 1199px;
    font-family: "Montserrat", sans-serif;
    color: var(--ink);
  }
  .label {
    position: absolute;
    left: 420px;
    top: 110px;
    width: 320px;
    height: 960px;
  }
  .brand-name {
    position: absolute;
    right: 0;
    bottom: 300px;
    writing-mode: vertical-rl;
    transform: rotate(180deg);
    font-weight: 500;
    font-size: 104px;
    line-height: 1;
    letter-spacing: 0.5px;
    color: var(--ink);
  }
  .product-info {
    position: absolute;
    right: 0;
    bottom: 0;
    text-align: right;
    color: var(--ink);
  }
  .flavour {
    font-weight: 700;
    font-size: 36px;
    line-height: 1.1;
    letter-spacing: 0.5px;
  }
  .claim {
    font-weight: 400;
    font-size: 29px;
    line-height: 1.25;
    letter-spacing: 0.3px;
    margin-bottom: 6px;
  }
  .features {
    list-style: none;
    font-weight: 400;
    font-size: 19px;
    line-height: 1.45;
    color: var(--ink-soft);
  }
</style>
</head>
<body>
  <main class="canvas">
    <section class="label">
      <div class="brand-name">verdalis</div>
      <div class="product-info">
        <h1 class="flavour">APPLE</h1>
        <p class="claim">ULTRA-FRESH</p>
        <ul class="features">
          <li>Handmade</li>
          <li>No preservatives</li>
          <li>Not heat-treated</li>
          <li>No added sugar</li>
        </ul>
      </div>
    </section>
  </main>
</body>
</html>
```